card for handyman and landscaping business, double sided with services listed on the back

Design a business card for a handyman and Landscaping business in San Jose,ca. Would like front to be a house with 3D characters doing different tasks i.e. Mowing lawn, painting, sprinklers, lighting, weed whacking, power washing, lumber etc. on the backside a cutout of the interior with computer, internet, cleaning, bathroom/kitchen remodeling, smart home etc.

Industry/Entity Type

Handyman

Contact Information for Business Card

Two sided view of a house, one outside services and one inside services

Colors

Designer to choose colors to be used in the design.

Requirements
Must have
• General Household Repairs and Maintenance
• Landscaping, Gardening, and Planting
• Painting, Patching and Trim/Moulding Work
• Cleaning, Restoring and Hauling/Trash Removal
• Blinds, Curtains, and Assembly Work
• Computer, Internet/Wireless, and Smart Home Service

```html
<!DOCTYPE html>
<html lang="en">
<head>
<meta charset="utf-8">
<title>Handyman &amp; Landscaping Business – Business Card</title>
<link rel="stylesheet" href="https://fonts.googleapis.com/css2?family=Open+Sans:ital,wght@0,300;0,400;0,600;0,700;1,700&display=swap">
<style>
  :root {
    --page-bg: #e9e9e9;
    --card-dark: #262324;
    --card-shade: #302c2d;
    --brown: #7a3c17;
    --cream: #f6c99a;
    --tan: #e7a774;
    --white: #f4f1ee;
    --muted: #bdb6b0;
  }
  * { margin: 0; padding: 0; box-sizing: border-box; }
  html, body { width: 1200px; height: 1200px; overflow: hidden; }
  body {
    background: var(--page-bg);
    font-family: "Open Sans", Arial, sans-serif;
    display: flex;
    flex-direction: column;
    align-items: center;
    justify-content: center;
    gap: 56px;
  }
  .card {
    position: relative;
    width: 900px;
    height: 514px;
    background: var(--card-dark);
    overflow: hidden;
    box-shadow: 0 6px 18px rgba(0,0,0,.25);
  }
  .card svg.frame { position: absolute; inset: 0; }

  /* front */
  .workers-art {
    position: absolute;
    left: 30px; top: 110px;
    width: 560px; height: 390px;
    background: radial-gradient(ellipse at 45% 55%, #38333400 0%, #3a353680 50%, transparent 75%);
    opacity: .8;
  }
  .identity { position: absolute; left: 64px; top: 150px; color: var(--white); }
  .identity .name { font-size: 46px; font-weight: 300; letter-spacing: 1px; }
  .identity .role { font-size: 20px; font-weight: 400; color: var(--muted); margin-top: 4px; }
  .identity .rule { width: 470px; height: 1px; background: var(--muted); margin: 16px 0 18px; }
  .contacts { list-style: none; }
  .contacts li { display: flex; align-items: center; gap: 12px; font-size: 19px; margin-bottom: 9px; }
  .contacts svg { width: 18px; height: 18px; flex: none; }
  .website {
    position: absolute; left: 430px; bottom: 40px;
    color: var(--white); font-size: 27px; font-weight: 700; font-style: italic;
  }
  .brand-mark {
    position: absolute; left: 570px; top: 150px; width: 240px;
    display: flex; flex-direction: column; align-items: center; gap: 12px;
    text-align: center;
  }
  .brand-mark .dot { width: 70px; height: 70px; border-radius: 50%; background: var(--brown); }
  .brand-mark .label { color: var(--tan); font-size: 20px; font-weight: 700; line-height: 1.25; text-transform: uppercase; }

  /* back */
  .character-art {
    position: absolute; left: 250px; top: 40px; width: 420px; height: 440px;
    background: radial-gradient(ellipse at 50% 45%, #3a3536 0%, #2f2b2c 50%, transparent 75%);
  }
  .back-title {
    position: absolute; left: 0; right: 0; top: 78px; text-align: center;
    color: var(--tan); text-transform: uppercase;
  }
  .back-title .main { font-size: 46px; font-weight: 700; letter-spacing: 1px; }
  .back-title .sub { font-size: 22px; font-weight: 700; letter-spacing: 3px; display: flex; align-items: center; justify-content: center; gap: 16px; margin-top: 4px; }
  .back-title .sub::before, .back-title .sub::after { content: ""; width: 110px; height: 3px; background: var(--tan); }
  .services {
    position: absolute; left: 0; right: 0; top: 250px; list-style: none;
    text-align: center; color: var(--white); font-size: 21px; line-height: 1.75;
  }
</style>
</head>
<body>

<section class="card card-front" aria-label="Business card front">
  <svg class="frame" viewBox="0 0 900 514" aria-hidden="true">
    <rect width="900" height="514" fill="var(--brown)"/>
    <path d="M0 96 L560 96 L690 30 L820 96 L860 96 L860 514 L0 514 Z" fill="var(--card-dark)"/>
    <path d="M0 90 L560 90 L690 24 L820 90 L860 90" fill="none" stroke="var(--cream)" stroke-width="5"/>
  </svg>
  <div class="workers-art" role="img" aria-label="Faint silhouettes of workers painting, climbing a ladder and doing yard work"></div>

  <div class="identity">
    <h1 class="name">JOHN DOE</h1>
    <p class="role">Director</p>
    <div class="rule"></div>
    <ul class="contacts">
      <li><svg viewBox="0 0 20 20"><circle cx="10" cy="10" r="10" fill="var(--tan)"/><path d="M7 5l2 3-1.2 1.2a6 6 0 003 3L12 11l3 2-1 2c-4 0-9-5-9-9z" fill="var(--card-dark)"/></svg>1-234-567890</li>
      <li><svg viewBox="0 0 20 20"><circle cx="10" cy="10" r="10" fill="var(--tan)"/><rect x="5" y="6.5" width="10" height="7" fill="var(--card-dark)"/><path d="M5 6.5l5 4 5-4" stroke="var(--tan)" fill="none"/></svg>john@companyname.com</li>
      <li><svg viewBox="0 0 20 20"><circle cx="10" cy="10" r="10" fill="var(--tan)"/><path d="M10 4a4 4 0 00-4 4c0 3 4 8 4 8s4-5 4-8a4 4 0 00-4-4z" fill="var(--card-dark)"/><circle cx="10" cy="8" r="1.5" fill="var(--tan)"/></svg>Dummy city, Dummy Country Land</li>
    </ul>
  </div>

  <div class="brand-mark">
    <span class="dot"></span>
    <span class="label">Handyman &amp; Landscaping Business</span>
  </div>

  <p class="website">www.companyname.com</p>
</section>

<section class="card card-back" aria-label="Business card back">
  <div class="character-art" role="img" aria-label="Faint silhouette of a handyman holding tools"></div>
  <header class="back-title">
    <h2 class="main">Handyman &amp; Landscaping</h2>
    <p class="sub">Business</p>
  </header>
  <ul class="services">
    <li>Handyman | Landscaping</li>
    <li>Sprinklers - Irrigation | Painting | Electrical | Lighting | Power Washing | Hauling</li>
    <li>Cleaning | Bath - Kitchen | Baseboards- Trim - Moulding</li>
    <li>Smart Home | A/C and Heating | Blinds | Curtains | Assembly Services | Computer - Tech Service</li>
  </ul>
</section>

</body>
</html>
```